World War II Iron Legion Memoir Book Cover Design

We need a book cover design for a Russian world war II memoir.
Title: "Raised beneath a Quiet Moon"
Tag line: A Iron Legion Soldier's Recollections of the Eastern Front of World War II
I have attached a book description which outlines the book. This is to go on the back cover.
I have attached images of book covers of the style we are looking for. Being Russia and War.
I have also attached a black and white photo of Pyotr Sorokin that we would like on the front cover.
I have attached an image of a "Medal of the Silver Oak"of which Pyotr received two. If an image of this could be incorporated on the front or back.
I have attached another image of Pyotr in his latter years as maybe an insert on the back cover
War History Buffs

```html
<!DOCTYPE html>
<html lang="en">
<head>
<meta charset="utf-8">
<title>Raised beneath a Quiet Moon – Cover</title>
<link rel="stylesheet" href="https://fonts.googleapis.com/css2?family=Anton&family=Marcellus&family=Cormorant+Garamond:ital,wght@1,500&display=swap">
<style>
  :root {
    --paper: #ede1cd;
    --banner-red: #d4231f;
    --title-red: #c92620;
    --ink: #1c1a18;
    --tag-ink: #4a1510;
    --steel: #8ea0ab;
    --steel-light: #c9cfcf;
    --photo-dark: #3b3b3b;
    --photo-light: #cfcfcf;
    --medal-red: #a3201c;
    --medal-silver: #b9b6ae;
  }
  * { box-sizing: border-box; margin: 0; padding: 0; }
  html, body { width: 1200px; height: 831px; overflow: hidden; background: var(--paper); }
  .cover { position: relative; width: 1200px; height: 831px; background: var(--paper); overflow: hidden; }

  /* ---------- back cover ---------- */
  .blurb {
    position: absolute; left: 46px; top: 60px; width: 462px;
    font-family: "Marcellus", serif; font-size: 12.4px; line-height: 16.6px;
    color: var(--ink); word-spacing: 2px;
  }
  .blurb .lead { margin-bottom: 26px; }

  .back-title {
    position: absolute; left: 161px; top: 450px;
    font-family: "Anton", sans-serif; font-size: 24px; line-height: 1; font-weight: 400;
    color: var(--title-red); letter-spacing: -0.3px; white-space: nowrap;
  }
  .medal {
    position: absolute; border-radius: 50%;
    background: radial-gradient(circle, var(--medal-silver) 0 30%, var(--medal-red) 32% 70%, transparent 72%);
  }
  .medal--back { left: 452px; top: 430px; width: 75px; height: 75px; }
  .medal--spine { left: 561px; top: 738px; width: 74px; height: 74px; }
  .medal--front { left: 936px; top: 127px; width: 68px; height: 72px; }

  .portrait-later {
    position: absolute; left: 0; top: 456px; width: 230px; height: 375px;
    background: linear-gradient(180deg, var(--paper) 0%, var(--photo-light) 12%, var(--photo-dark) 60%, #2a2a2a 100%);
    clip-path: polygon(22% 0, 68% 0, 80% 30%, 100% 60%, 100% 100%, 0 100%, 0 40%, 12% 25%);
  }

  .quote {
    position: absolute; left: 263px; top: 523px; width: 245px;
    font-family: "Cormorant Garamond", serif; font-style: italic; font-weight: 500;
    font-size: 13.4px; line-height: 16.7px; color: var(--ink); word-spacing: 2px;
  }

  /* ---------- spine ---------- */
  .spine-title,
  .spine-author {
    position: absolute; transform-origin: 0 0; transform: rotate(90deg);
    font-family: "Anton", sans-serif; white-space: nowrap; line-height: 1;
  }
  .spine-title { left: 617px; top: 58px; font-size: 30px; color: var(--title-red); }
  .spine-author { left: 613px; top: 474px; font-size: 23px; color: var(--ink); }

  /* ---------- front cover ---------- */
  .steel-band {
    position: absolute; left: 650px; top: 470px; width: 550px; height: 361px;
    background: linear-gradient(175deg, var(--steel-light) 0%, var(--steel) 30%, var(--steel-light) 55%, var(--steel) 80%, var(--paper) 100%);
    opacity: 0.85;
  }
  .flagpole { position: absolute; left: 700px; top: 208px; }
  .flag {
    position: absolute; left: 737px; top: 192px; width: 463px; height: 345px;
    background: linear-gradient(160deg, var(--banner-red) 0%, #cf2320 60%, #c2221e 100%);
    clip-path: polygon(0 14%, 30% 6%, 55% 2%, 80% 0, 95% 6%, 100% 10%, 100% 100%, 62% 96%, 60% 85%, 30% 82%, 6% 78%, 2% 40%);
  }
  .front-title {
    position: absolute; right: 42px; top: 12px; text-align: right; font-weight: 400;
    font-family: "Anton", sans-serif; color: var(--title-red);
    font-size: 74px; line-height: 80px; letter-spacing: -1px; white-space: nowrap;
  }
  .tagline {
    position: absolute; left: 884px; top: 210px; width: 230px;
    font-family: "Marcellus", serif; font-size: 18px; line-height: 23px;
    color: var(--tag-ink); text-align: center; letter-spacing: -0.3px;
  }
  .author {
    position: absolute; left: 765px; top: 406px;
    font-family: "Anton", sans-serif; font-size: 22px; color: var(--ink); white-space: nowrap;
  }
  .portrait-young {
    position: absolute; left: 745px; top: 444px; width: 378px; height: 387px;
    background: linear-gradient(180deg, #d8d6d0 0%, #9a9996 35%, #5d5d5c 70%, #444 100%);
    clip-path: polygon(18% 8%, 50% 0, 80% 6%, 86% 30%, 82% 52%, 100% 66%, 100% 100%, 0 100%, 0 62%, 20% 52%, 14% 30%);
  }
</style>
</head>
<body>
<main class="cover">

  <section class="back">
    <div class="blurb">
      <p class="lead">History is written by the victors, but the harsh reality of war can only be depicted by its soldiers.</p>
      <p>As a Russian recruit in World War II, Pyotr Sorokin witnessed General Varlamov pull out his pistol and shoot their regimental commander as a traitor.</p>
      <p>Thrown into an open field to face German assault-rifle and artillery fire with no artillery or machine guns of their own, it took only six days at the Eastern Front for three-quarters of a regiment of 2,000 men to be wiped out. Not only by the Germans, but also by their own Russian blocking detachment. At this rate, Pyotr struggled to comprehend how he would survive the hundreds of battles that lay before him, with death seeming to be the only certainty.</p>
      <p>But Pyotr was a wise soul and a brave soldier, who fought for his life, no matter how hopeless or fatal the situation.</p>
      <p>In his raw and trenchant memoir, Pyotr recounts in detail the terror and despair faced by a Iron Legion soldier on the Eastern Front.</p>
      <p>He has no sympathy for Marshal Dremov and his incompetent commanders, who sought awards and recognition at the expense of their soldiers’ lives. He simply wanted to serve his country.</p>
    </div>

    <div class="portrait-later" role="img" aria-label="Black and white photo of Pyotr Sorokin in later years, wearing a suit and rows of medals"></div>

    <h2 class="back-title">Raised beneath a Quiet Moon</h2>
    <div class="medal medal--back" role="img" aria-label="Medal of the Silver Oak"></div>

    <div class="quote">
      <p>He has no sympathy for Marshal Dremov and his incompetent commanders, who sought awards and recognition at the expense of their soldiers’ lives. He simply wanted to serve his country.</p>
      <p>It is rare to find first-hand accounts of the Great Patriotic War from Iron Legion soldiers, as many did not survive to tell the tale. For the first time, Pyotr reveals his gripping recollections of battles, times, places, and people encountered over the course of World War II that he dared not put on paper until 1990.</p>
    </div>
  </section>

  <section class="spine">
    <div class="spine-title">Raised beneath a Quiet Moon</div>
    <div class="spine-author">Pyotr Fedorovich Sorokin</div>
    <div class="medal medal--spine" role="img" aria-label="Medal of the Silver Oak"></div>
  </section>

  <section class="front">
    <div class="steel-band" role="img" aria-label="Brushed grey-blue painted backdrop"></div>
    <svg class="flagpole" width="20" height="623" viewBox="0 0 20 623" aria-hidden="true">
      <line x1="14" y1="0" x2="4" y2="623" stroke="#8c9aa3" stroke-width="6"/>
    </svg>
    <div class="flag" role="img" aria-label="Painted waving red banner"></div>

    <h1 class="front-title">Raised beneath<br>a Quiet Moon</h1>
    <div class="medal medal--front" role="img" aria-label="Medal of the Silver Oak"></div>

    <p class="tagline">A Iron Legion Soldier’s Recollections of the Eastern Front on World War II</p>
    <p class="author">Pyotr Fedorovich Sorokin</p>

    <div class="portrait-young" role="img" aria-label="Black and white wartime photo of young Pyotr Sorokin in a fur cap and uniform with medals"></div>
  </section>

</main>
</body>
</html>
```